KAPK Poster

Action Thriller Suspense Film Poster

It is a feature Film Poster titled : KAPK ; KHOJ 450 ARAB PAUND KI aka in search of 450 arab pounds

It should be marcus Vale or Operation Nightglass type

Fb Page: #kapkthe film

Target Market(s)

18-40

Requirements
Must have
• thrill
Nice to have
• production value
Should not have
• comic touches

```html
<!DOCTYPE html>
<html lang="en">
<head>
<meta charset="utf-8">
<title>KAPK — Khoj 450 Arab Paund Ki</title>
<link rel="stylesheet" href="https://fonts.googleapis.com/css2?family=Cinzel:wght@400;500;600&family=Oswald:wght@400;500&display=swap">
<style>
  :root {
    --ink: #050505;
    --silver-hi: #eef2f6;
    --silver-mid: #9aa6b2;
    --silver-lo: #4c5560;
    --ornament: #c9ced6;
    --ornament-dark: #2a2d31;
    --credit: #b9c0c8;
    --credit-dim: #7d848c;
  }
  * { margin: 0; padding: 0; box-sizing: border-box; }
  html, body {
    width: 960px; height: 1200px; overflow: hidden;
    background: var(--ink);
  }
  .poster {
    position: relative;
    width: 960px; height: 1200px;
    background: var(--ink);
    overflow: hidden;
  }
  .ornament-band {
    position: absolute; left: 0; width: 960px;
  }
  .ornament-band--top {
    top: 0; height: 190px;
    background: linear-gradient(180deg, var(--ornament) 0%, #8d939b 14%, var(--ornament-dark) 30%, #6f757d 55%, #1a1c1f 100%);
  }
  .ornament-band--bottom {
    bottom: 0; height: 210px;
    background: linear-gradient(0deg, var(--ornament) 0%, #8d939b 12%, var(--ornament-dark) 28%, #6f757d 55%, #141518 100%);
  }
  .ornament-scroll {
    position: absolute; bottom: 150px; width: 150px; height: 110px;
    background: radial-gradient(ellipse at center, #8a9098 0%, #3a3e43 60%, transparent 75%);
  }
  .ornament-scroll--left { left: 0; }
  .ornament-scroll--right { right: 0; }

  .title {
    position: absolute; left: 0; top: 330px; width: 960px;
    text-align: center;
    font-family: "Cinzel", serif;
    font-weight: 500;
    line-height: 0.9;
  }
  .title__line {
    display: block;
    background: linear-gradient(180deg, var(--silver-hi) 0%, var(--silver-mid) 45%, var(--silver-lo) 60%, var(--silver-hi) 100%);
    -webkit-background-clip: text; background-clip: text;
    color: transparent;
  }
  .title__line--lead { font-size: 118px; letter-spacing: 4px; }
  .title__line--figure { font-size: 230px; letter-spacing: -6px; position: relative; }
  .title__line--mid { font-size: 138px; letter-spacing: 2px; }
  .title__line--tail { font-size: 92px; letter-spacing: 2px; margin-top: 6px; }

  .glass-crack {
    position: absolute; left: 472px; top: 545px;
    width: 110px; height: 110px; border-radius: 50%;
    background: radial-gradient(circle, #000 0%, #000 16%, #3a4048 22%, #14171b 55%, transparent 72%);
  }

  .credits {
    position: absolute; left: 0; top: 905px; width: 960px;
    text-align: center;
    font-family: "Oswald", sans-serif;
    color: var(--credit);
    font-size: 13px; letter-spacing: 1px; line-height: 22px;
    text-transform: uppercase;
  }
  .credits__role { color: var(--credit-dim); font-size: 8px; margin: 0 3px 0 10px; }
  .credits__name { font-weight: 500; }
</style>
</head>
<body>
<main class="poster">
  <div class="ornament-band ornament-band--top" role="img" aria-label="Ornate silver lace border pattern"></div>

  <h1 class="title">
    <span class="title__line title__line--lead">KHOJ</span>
    <span class="title__line title__line--figure">450</span>
    <span class="title__line title__line--mid">ARAB</span>
    <span class="title__line title__line--tail">PAUND KI</span>
  </h1>

  <div class="glass-crack" role="img" aria-label="Bullet hole with shattered glass cracks"></div>

  <section class="credits">
    <p><span class="credits__role">a</span><span class="credits__name">Producers</span><span class="credits__role">film</span><span class="credits__name">Script Writer</span><span class="credits__role">starring</span><span class="credits__name">Actor One Actor Two</span></p>
    <p><span class="credits__role">costume</span><span class="credits__name">Designers Name</span><span class="credits__role">directed by</span><span class="credits__name">Directors Name</span><span class="credits__role">produced by</span><span class="credits__name">Producers Name</span><span class="credits__role">written by</span><span class="credits__name">Writer</span><span class="credits__role">production</span><span class="credits__name">Designers Name</span></p>
    <p><span class="credits__role">music by</span><span class="credits__name">Musician</span><span class="credits__role">animation by</span><span class="credits__name">Animator Name</span><span class="credits__role">director of photography</span><span class="credits__name">Photographers Name</span></p>
  </section>

  <div class="ornament-scroll ornament-scroll--left" role="img" aria-label="Silver scrollwork flourish"></div>
  <div class="ornament-scroll ornament-scroll--right" role="img" aria-label="Silver scrollwork flourish"></div>
  <div class="ornament-band ornament-band--bottom" role="img" aria-label="Ornate silver lace border with scrollwork"></div>
</main>
</body>
</html>
```